Personal Vistrano Banner

I am creating a personal brand for myself. I want a vistrano banner that inspires and motivates people to reach their epic awesomeness. I am creating and designing my personal brand. It can be a background with words on a scenery a picture or 3d graphic. If someone looked at it, they should say it is aggressively epic and motivating. It should be dramatic and bold.
My personal goal is to help as many people reach financial freedom as possible, and challenge and break their own limiting beliefs. This personal brand will be integrated into my zomblat, quorVex, and professional vistrano fanpage (in addition to personal page). My goals are to open up a school for the underpriveleged children, develop my network marketing company team, and become a billionaire in the process. I want to attract people to me that really identify with doing what most think is impossible in terms of personal growth, impact to the world and financial wealth.
Updates

I have updated my brief with more background, and added a new comment to the discussion section to give you more to work with.

Reason: To give designers more time and to create a second and third place prize.

Reason: I am giving designers time to submit more designs

Target Market(s)

business professionals, and people with an entrepreneurial spirit.

Industry/Entity Type

Financial

Requirements
Must have
• It must be the exact dimensions required for vistrano banners. It should not be bigger or smaller. exact!!!

```html
<!DOCTYPE html>
<html lang="en">
<head>
<meta charset="utf-8">
<title>Release Your EPIC Banner</title>
<link rel="stylesheet" href="https://fonts.googleapis.com/css2?family=Carlito&display=swap">
<style>
  :root {
    --bg: #000000;
    --word: #ffffff;
    --headline: #ff0000;
  }
  html, body {
    margin: 0;
    padding: 0;
    width: 1200px;
    height: 800px;
    overflow: hidden;
    background: var(--bg);
  }
  .banner {
    position: relative;
    width: 1200px;
    height: 800px;
    background: var(--bg);
    font-family: "Carlito", "Calibri", sans-serif;
    overflow: hidden;
  }
  .word {
    position: absolute;
    margin: 0;
    color: var(--word);
    font-size: 50px;
    line-height: 1;
    white-space: nowrap;
  }
  .headline {
    position: absolute;
    margin: 0;
    left: 229px;
    top: 315px;
    color: var(--headline);
    font-size: 77px;
    font-weight: 400;
    line-height: 1;
    white-space: nowrap;
  }
</style>
</head>
<body>
<main class="banner">
  <span class="word" style="left:3px;top:15px">breathtaking</span>
  <span class="word" style="left:317px;top:15px">fearsome</span>
  <span class="word" style="left:604px;top:15px">stunning</span>
  <span class="word" style="left:903px;top:15px">marvelous</span>

  <span class="word" style="left:3px;top:104px">inducement</span>
  <span class="word" style="left:347px;top:104px">powerful</span>
  <span class="word" style="left:621px;top:104px">amazing</span>
  <span class="word" style="left:864px;top:104px">mind-blowing</span>

  <span class="word" style="left:3px;top:195px">enthusiasm</span>
  <span class="word" style="left:315px;top:195px">stimulus</span>
  <span class="word" style="left:611px;top:195px">flexibility</span>
  <span class="word" style="left:903px;top:195px">impractical</span>

  <span class="word" style="left:3px;top:263px">independence</span>
  <span class="word" style="left:367px;top:263px">determination</span>
  <span class="word" style="left:745px;top:263px">enterprise</span>
  <span class="word" style="left:1067px;top:263px">drive</span>

  <span class="word" style="left:7px;top:348px">illimitable</span>
  <h1 class="headline">"Release Your EPIC"</h1>
  <span class="word" style="left:977px;top:348px">ambition,</span>

  <span class="word" style="left:7px;top:455px">infinite</span>
  <span class="word" style="left:224px;top:455px">unlimited</span>
  <span class="word" style="left:515px;top:455px">unbounded</span>
  <span class="word" style="left:868px;top:455px">boundless</span>

  <span class="word" style="left:3px;top:544px">interminable</span>
  <span class="word" style="left:349px;top:544px">inexhaustible</span>
  <span class="word" style="left:688px;top:544px">constant</span>
  <span class="word" style="left:937px;top:535px">perpetual</span>

  <span class="word" style="left:3px;top:615px">immeasurable</span>
  <span class="word" style="left:367px;top:615px">bottomless</span>
  <span class="word" style="left:692px;top:602px">fathomless</span>
  <span class="word" style="left:981px;top:592px">unceasing</span>

  <span class="word" style="left:3px;top:678px">endless</span>
  <span class="word" style="left:273px;top:678px">never-ending</span>
  <span class="word" style="left:653px;top:682px">unending</span>
  <span class="word" style="left:935px;top:668px">everlasting</span>

  <span class="word" style="left:3px;top:742px">ambitious</span>
  <span class="word" style="left:253px;top:742px">heroic</span>
  <span class="word" style="left:441px;top:738px">untold</span>
  <span class="word" style="left:613px;top:742px">Grand</span>
  <span class="word" style="left:783px;top:742px">Great</span>
  <span class="word" style="left:948px;top:735px">Herculean</span>
</main>
</body>
</html>
```